Travel Website Design

My client is a startup that will sell Ridgewater Expeditions and fishing trips.
We do not have a logo as of yet, but I have attached 3 options for you to use in the mockup process. Please feel free to use any one (or all 3) of them, but don't base design around them.

Also attached is client's loose idea of how he wants an interior page to look. For the homepage, it would definitely need a rotating image slider, a search, and a tabbed section. The bluecranereelcasting.com is probably closest to what he is looking for.

Here are a few websites to pass along. In addition to the logos I have attached some links of company websites that are competition and have similar designs and layouts similar to what I am looking for.

http://www.bluecranereelcasting.com - The most direct competition that I have. I really like how they layout the pages and lodges info.

Tarvo.com - Close competition. Not a huge fan of how they search for lodges but like how they display each lodge and provide info.

http://www.qirandel.com/ - Example of a company website and layout the client does not like.

http://stonebrookjourneys.com/ - Clean feel. Not a fan of how they layout each lodges info.

```html
<!DOCTYPE html>
<html lang="en">
<head>
<meta charset="utf-8">
<title>Ridgewater Expeditions – Home</title>
<link href="https://fonts.googleapis.com/css2?family=Ubuntu:ital,wght@0,400;0,500;0,700;1,400&family=Open+Sans:ital,wght@0,400;0,600;1,400;1,600&family=Oxygen:wght@400;700&family=Rubik:wght@700&display=swap" rel="stylesheet">
<style>
:root{
  --blue:#0b6e9c;
  --blue-light:#1184b6;
  --blue-dark:#08577c;
  --ink:#222;
  --text:#3a3a3a;
  --black:#161616;
  --page:#e7e7ec;
  --panel:#f0f0f5;
  --footer:#1d1d1d;
  --white:#fff;
}
*{box-sizing:border-box;margin:0;padding:0}
html,body{width:1005px;height:1200px;overflow:hidden}
body{position:relative;background:var(--page);font-family:"Oxygen",sans-serif;color:var(--text)}
.abs{position:absolute}

/* header */
.topline{left:0;top:0;width:1005px;height:6px;background:var(--black)}
.header{left:0;top:6px;width:1005px;height:97px;background:var(--white)}
.member-tab{left:572px;top:6px;width:148px;height:28px;background:var(--black);border-radius:0 0 4px 4px;color:#fff;font:500 13px "Ubuntu",sans-serif;text-align:center;line-height:27px;transform:skewX(0)}
.social-tab{left:740px;top:6px;width:147px;height:28px;background:var(--black);border-radius:0 0 4px 4px;display:flex;gap:12px;justify-content:center;align-items:center}
.social-tab span{width:22px;height:22px;border-radius:3px;background:#3b7cc4}
.brand{left:117px;top:22px;display:flex;align-items:center;gap:12px}
.brand-mark{width:70px;height:70px;border-radius:50%;background:var(--blue)}
.brand-name{font:700 26px/28px "Rubik",sans-serif;color:var(--ink)}
.quote{right:116px;top:71px;font:500 19px "Ubuntu",sans-serif;color:var(--blue);display:flex;align-items:center;gap:6px}
.quote b{color:var(--ink);font-weight:500}
.quote .num{color:var(--ink);margin-left:8px}

/* nav */
.navline{left:0;top:103px;width:1005px;height:5px;background:var(--black)}
.nav{left:0;top:108px;width:1005px;height:37px;background:linear-gradient(#1483b3,#0a628b)}
.nav ul{list-style:none;position:absolute;left:117px;top:0;display:flex;height:37px}
.nav li{font:500 12.5px/35px "Ubuntu",sans-serif;color:#d7ecf6;text-align:center;border-right:1px solid rgba(0,0,0,.25)}
.nav li.active{background:var(--black);color:#fff}

/* hero */
.hero{left:0;top:145px;width:1005px;height:375px;background:linear-gradient(180deg,#c58a34 0%,#e9a93c 35%,#7a5a2c 58%,#b7822f 72%,#3e3424 100%)}
.hero-title{left:398px;top:210px;font:italic 400 24px/30px "Open Sans",sans-serif;color:#fff;text-shadow:1px 1px 3px rgba(0,0,0,.6)}
.finder{left:0;top:450px;width:1005px;height:28px;background:rgba(20,20,20,.75);border-bottom:1px solid var(--blue-light)}
.finder-label{left:139px;top:453px;font:500 17px "Ubuntu",sans-serif;color:#fff}
.finder-btn{left:418px;top:450px;width:215px;height:28px;background:var(--blue);color:#fff;font:500 17px/28px "Ubuntu",sans-serif;text-align:center}
.dots{left:793px;top:459px;display:flex;gap:5px}
.dots i{width:10px;height:10px;border-radius:50%;background:#fff}
.dots i.on{background:var(--blue-light)}

/* content panel */
.panel{left:121px;top:486px;width:762px;height:517px;background:var(--panel);border-radius:4px}
.welcome{left:139px;top:510px;display:flex;align-items:center;gap:8px;font:400 18px "Ubuntu",sans-serif;color:var(--blue)}
.welcome .dot{width:22px;height:22px;border-radius:50%;background:var(--blue)}
.welcome b{font:700 18px "Rubik",sans-serif;color:var(--ink)}
.rule{left:139px;top:541px;width:526px;border-top:1px dotted #777}
.intro{left:140px;top:547px;width:527px;font-size:11.3px;line-height:17px;color:#333}
.intro p{margin-bottom:8px}
.testi-head{left:697px;top:494px;width:161px;height:26px;background:var(--blue);color:#fff;font:500 14px/26px "Ubuntu",sans-serif;text-align:center}
.testi{left:690px;top:520px;width:175px;height:190px;border:1px solid #cfcfd6;border-radius:4px;background:#f3f3f7}
.testi q{position:absolute;left:13px;top:18px;width:152px;font:italic 11.3px/17px "Open Sans",sans-serif;color:#333;quotes:none}
.testi .name{position:absolute;left:13px;top:136px;font:600 12px "Open Sans",sans-serif;color:#222}
.btn{background:var(--blue);color:#fff;font:11px "Oxygen",sans-serif;border-radius:2px}
.testi .btn{position:absolute;left:13px;top:163px;width:58px;height:18px;line-height:18px;text-align:center}

.card{top:731px;width:172px}
.card h3{font:500 18px "Ubuntu",sans-serif;color:var(--ink);margin-left:5px}
.card h3 span{color:var(--blue)}
.card .photo{margin-top:7px;height:100px;border:4px solid #fff;box-shadow:0 1px 3px rgba(0,0,0,.25)}
.card p{margin:19px 0 0 6px;font:11.3px/13px "Open Sans",sans-serif;letter-spacing:.5px;color:#333}
.card .more{position:absolute;right:0;top:199px;display:flex;height:17px}
.card .more span{width:68px;line-height:17px;text-align:center;border-radius:2px 0 0 2px}
.card .more i{width:16px;background:#333;border-radius:0 2px 2px 0;color:#fff;font:normal 10px/17px sans-serif;text-align:center}

/* footer */
.footer{left:0;top:982px;width:1005px;height:175px;background:var(--footer);z-index:-0}
.panel,.panel~*{z-index:1}
.fcol{top:1018px;color:#eee}
.fcol h4{font:500 13px "Ubuntu",sans-serif;margin-bottom:8px}
.links{list-style:none;font-size:10.5px;line-height:17.8px}
.links li::before{content:"› ";}
.fdiv{top:1030px;width:1px;height:100px;background:#3a3a3a}
.field{width:168px;height:20px;background:#fff;border:1px solid #999;font-size:10px;line-height:18px;padding-left:7px;color:#444;margin-bottom:8px}
.submit{width:78px;height:20px;line-height:20px;text-align:center;font:700 12px "Ubuntu",sans-serif;margin-top:1px}
.crow{display:flex;gap:10px;font-size:10.5px;line-height:14px;padding:7px 0;border-bottom:1px dotted #666;width:180px}
.crow:last-child{border:none}
.crow svg{flex:none}
.footer-mark{left:784px;top:1040px;width:76px;height:76px;border-radius:50%;background:#26405a;opacity:.7}
.bottom{left:0;top:1157px;width:1005px;height:43px;background:var(--blue)}
.copy{left:142px;top:1171px;color:#fff;font:500 10.5px "Ubuntu",sans-serif}
.connect{left:641px;top:1166px;display:flex;align-items:center;gap:12px;color:#fff;font:500 10.5px "Ubuntu",sans-serif}
.connect span{width:22px;height:22px;border-radius:3px;background:#3b7cc4}
</style>
</head>
<body>
<div class="abs topline"></div>
<header class="abs header"></header>
<div class="abs member-tab">Become A Member</div>
<div class="abs social-tab" aria-label="Social links"><span></span><span></span><span></span><span></span></div>
<div class="abs brand"><div class="brand-mark"></div><div class="brand-name">Ridgewater<br>Expeditions</div></div>
<div class="abs quote">Request a <b>FREE</b> Quote
  <svg width="18" height="20" viewBox="0 0 18 20"><path d="M4 2l4 4-2 2c1 3 3 5 6 6l2-2 4 4-3 3C8 18 1 11 1 5z" fill="#222"/></svg>
  Call: <span class="num">1.555.010.4420</span></div>

<div class="abs navline"></div>
<nav class="abs nav"><ul>
  <li class="active" style="width:101px">Home</li>
  <li style="width:144px">About Us</li>
  <li style="width:170px">Conversation</li>
  <li style="width:119px">Blog</li>
  <li style="width:130px">Travel</li>
  <li style="width:155px;border:none">Contact Us</li>
</ul></nav>

<section class="abs hero" role="img" aria-label="Angler silhouetted with a fishing rod on a river at sunset"></section>
<h1 class="abs hero-title">Take Your Time And View The Fantastic Fly<br>Fishing And Sport Fishing Destinations.</h1>
<div class="abs finder"></div>
<div class="abs finder-label">WHERE DO YOU WANT TO FISH?</div>
<div class="abs finder-btn">CHOOSE DESTINATION &#9650;</div>
<div class="abs dots"><i></i><i class="on"></i><i></i><i></i><i></i></div>

<div class="abs footer"></div>
<main class="abs panel"></main>
<h2 class="abs welcome"><span class="dot"></span>Welcome to <b>Ridgewater Expeditions</b></h2>
<div class="abs rule"></div>
<div class="abs intro">
  <p>Lorem ipsum dolor sit amet, consectetuer adipiscing elit, sed diam nonummy nibh euismod tincidunt ut laoreet dolore magna aliquam erat volutpat. Ut wisi enim ad minim veniam, quis nostrud exerci tation ullamcorper suscipit lobortis nisl ut aliquip ex ea commodo consequat. Duis autem vel eum iriure dolor in hendrerit in vulputate velit esse molestie consequat.</p>
  <p>Lorem ipsum dolor sit amet, consectetuer adipiscing elit, sed diam nonummy nibh euismod tincidunt ut laoreet dolore magna aliquam erat volutpat. Ut wisi enim ad minim veniam, quis nostrud exerci tation ullamcorper suscipit lobortis nisl ut aliquip ex ea commodo consequat. Duis autem vel eum iriure dolor in hendrerit in vulputate velit esse molestie consequat.</p>
</div>

<div class="abs testi-head">Testimonials</div>
<aside class="abs testi">
  <q>&ldquo; Lorem ipsum dolor sit amet consetug e sed diay nibh euismodl tincidunt ut laoreet dolore magam er vol wisi enim ad minim veniam quis nostrud exerci &rdquo;</q>
  <div class="name">Mr.Elliot Marsh</div>
  <div class="btn">View All</div>
</aside>

<article class="abs card" style="left:138px">
  <h3>Travel <span>Blog</span></h3>
  <div class="photo" role="img" aria-label="Two anglers standing in a river" style="background:linear-gradient(#4f7a3c,#8aa6a0)"></div>
  <p>Lorem ipsum dolor sit amet consectetuer adipiscing elit, sed diam nonummy nibh</p>
  <div class="more"><span class="btn">Read More</span><i>»</i></div>
</article>
<article class="abs card" style="left:322px">
  <h3>Specials <span>&amp; Deals</span></h3>
  <div class="photo" role="img" aria-label="Angler in a raft on a forest lake" style="background:linear-gradient(#3d9ad8,#2f5f3a 55%,#2a6b8a)"></div>
  <p>Lorem ipsum dolor sit amet consectetuer adipiscing elit, sed diam nonummy nibh</p>
  <div class="more"><span class="btn">Read More</span><i>»</i></div>
</article>
<article class="abs card" style="left:507px">
  <h3>Hosted <span>&amp; Trips</span></h3>
  <div class="photo" role="img" aria-label="Anglers casting from a boat at sea" style="background:linear-gradient(#5fb0e6,#2f7fbf 60%,#1c5f93)"></div>
  <p>Lorem ipsum dolor sit amet consectetuer adipiscing elit, sed diam nonummy nibh</p>
  <div class="more"><span class="btn">Read More</span><i>»</i></div>
</article>
<article class="abs card" style="left:692px">
  <h3>Couples<span>/Family</span></h3>
  <div class="photo" role="img" aria-label="Couple on a boat holding their catch" style="background:linear-gradient(#4aa3dc,#9fb6a4 55%,#e9e9e9)"></div>
  <p>Lorem ipsum dolor sit amet consectetuer adipiscing elit, sed diam nonummy nibh</p>
  <div class="more"><span class="btn">Read More</span><i>»</i></div>
</article>

<div class="abs fcol" style="left:138px">
  <h4>Quick Links</h4>
  <ul class="links"><li>Home</li><li>About Us</li><li>Conversation</li><li>Blog</li><li>Travel</li><li>Contact Us</li></ul>
</div>
<div class="abs fdiv" style="left:253px"></div>
<div class="abs fcol" style="left:288px">
  <h4>Sign Up For Newsletter</h4>
  <div style="font-size:9.5px;margin:-1px 0 8px">Sign up to recieive our free newsletters!</div>
  <div class="field">Name</div>
  <div class="field">Email Address</div>
  <div class="btn submit">SUBMIT</div>
</div>
<div class="abs fdiv" style="left:493px"></div>
<div class="abs fcol" style="left:528px">
  <h4 style="margin-bottom:2px">Contact Information</h4>
  <div class="crow"><svg width="13" height="16" viewBox="0 0 13 16"><path d="M6.5 0A6 6 0 0 0 .5 6c0 4 6 10 6 10s6-6 6-10a6 6 0 0 0-6-6zm0 8.5a2.5 2.5 0 1 1 0-5 2.5 2.5 0 0 1 0 5z" fill="#1184b6"/></svg><span>Lorem Ipsum is simply dummy and typesetting industry.</span></div>
  <div class="crow"><svg width="13" height="14" viewBox="0 0 18 20"><path d="M4 2l4 4-2 2c1 3 3 5 6 6l2-2 4 4-3 3C8 18 1 11 1 5z" fill="#1184b6"/></svg><span>info@ridgewaterexpeditions.com</span></div>
  <div class="crow"><svg width="13" height="12" viewBox="0 0 13 10"><rect width="13" height="10" fill="#1184b6"/><path d="M0 0l6.5 5L13 0" stroke="#1d1d1d" fill="none"/></svg><span>1.555.010.4420</span></div>
</div>
<div class="abs fdiv" style="left:746px"></div>
<div class="abs footer-mark"></div>

<footer class="abs bottom"></footer>
<div class="abs copy">© 2014 Ridgewater Expeditions All Rights Reserved.</div>
<div class="abs connect">Connected with Us <span></span><span></span><span></span><span></span></div>
</body>
</html>
```